KalVeno Website- Joomla Template

A website for a Plumber company. A one page design ( this is what i mean http://vollantiwerk.example/en/#graph)
The website should be a template for Joomla, i will do the website in 3 languages
I want it to be elegant but not so that it looks like a consulting company.
My customers are private customers, my products are :
Main focus is on Fixing 24/7
then renovate bathrooms
replace heating systems
and Maintenance
I need 12 slides:
Who we are
News
Service
Maintenance
Renewable Energy
Sanitary
Heating
Ventilation
Partners
Useful Links
Contact us
of course a Facebook, twitter and G+ icon
try to make an innovative nice menu

```html
<!DOCTYPE html>
<html lang="en">
<head>
<meta charset="utf-8">
<title>KalVeno Plumbing</title>
<link rel="stylesheet" href="https://fonts.googleapis.com/css2?family=Noto+Serif:wght@400;700&family=Open+Sans:wght@300;400;600&display=swap">
<style>
:root{
  --blue:#1d5b94;
  --green:#3bb54a;
  --ink:#333333;
  --muted:#555555;
  --paper:#efefef;
  --paper-alt:#f4f4f4;
  --white:#ffffff;
  --dark:#2d2d2d;
  --field:#3d3d3d;
  --line:#d9d9d9;
}
*{margin:0;padding:0;box-sizing:border-box}
html,body{width:1200px;height:3597px;overflow:hidden}
body{position:relative;background:var(--paper);color:var(--ink);font-family:"Noto Serif",Georgia,serif}
section,header{position:absolute;left:0;width:1200px}
.center{text-align:center}

/* hero */
.hero{top:0;height:586px;background:linear-gradient(135deg,#5a4636 0%,#3d3a38 40%,#6b5b4b 70%,#2e2c2b 100%)}
.hero-photo{position:absolute;inset:0}
.hero-shade{position:absolute;inset:0;background:rgba(0,0,0,.25)}
.hero-brand{position:absolute;top:120px;left:0;width:1200px;text-align:center;color:var(--white)}
.hero-mark{width:110px;height:110px;border:5px solid var(--white);border-radius:50%;margin:0 auto 16px}
.hero-name{font-size:62px;letter-spacing:3px;font-weight:400;font-variant:small-caps}
.hero-tagline{margin-top:8px;color:var(--green);font-size:15px;letter-spacing:5px;font-family:"Open Sans",Arial,sans-serif}
.hero-badge{position:absolute;left:560px;top:420px;width:80px;height:80px;border:3px solid var(--green);border-radius:50%;color:var(--green);text-align:center;font-family:"Open Sans",Arial,sans-serif;font-size:15px;font-weight:600;line-height:18px;padding-top:20px}
.hero-dots{position:absolute;top:548px;left:555px;display:flex;gap:10px}
.hero-dots span{width:10px;height:10px;border-radius:50%;background:rgba(255,255,255,.6)}
.hero-dots span.active{background:var(--white)}
.hero-scroll{position:absolute;right:45px;top:470px}

/* header */
.site-header{top:586px;height:77px;background:var(--white);border-bottom:1px solid var(--line)}
.header-brand{position:absolute;left:145px;top:20px;display:flex;align-items:center;gap:10px;color:var(--blue);font-size:26px}
.brand-dot{width:36px;height:36px;border:3px solid var(--blue);border-radius:50%}
.social{position:absolute;right:140px;top:22px;display:flex;gap:14px}
.social span{width:32px;height:32px;border-radius:50%;background:#b5b5b5}
.social span.on{background:#3a87c8}

/* headings */
.section-title{font-size:38px;font-weight:400;letter-spacing:1px}
.section-sub{font-size:13px;margin-top:2px}

/* about */
.about{top:663px;height:327px;background:var(--paper-alt)}
.about .section-title{color:var(--blue);font-family:"Open Sans",Arial,sans-serif;font-weight:600;margin-top:50px}
.about-text{width:850px;margin:22px auto 0;font-size:12.5px;line-height:17px;color:var(--muted);text-align:center}
.about-text p{margin-bottom:14px}

/* news */
.news{top:990px;height:316px;background:linear-gradient(180deg,#4f87ad 0%,#2f6e96 55%,#6ea2c2 100%)}
.news-photo{position:absolute;inset:0}
.news .section-title{position:relative;color:var(--white);margin-top:30px;font-size:40px}
.news-cards{position:absolute;top:102px;left:160px;display:flex;gap:18px}
.news-card{width:162px;height:185px;background:var(--white);text-align:center;padding:6px}
.news-thumb{height:46px;background:linear-gradient(90deg,#9aa5ae,#cfd6db,#7f8b94)}
.news-card h3{font-size:14px;margin-top:8px}
.news-card p{font-size:11px;line-height:13px;color:var(--muted);margin-top:3px}
.news-card a{display:block;color:var(--green);font-size:11px;margin-top:6px;text-decoration:none}

/* services */
.services{top:1306px;height:724px;background:var(--paper)}
.services .section-title{margin-top:60px}
.service{position:absolute;width:300px;text-align:center}
.service svg{display:block;margin:0 auto}
.service h3{font-size:19px;font-weight:400;margin-top:14px}
.service p{font-size:12.5px;line-height:16px;color:var(--muted);margin-top:8px}

/* partners */
.partners{top:2030px;height:317px;background:var(--white)}
.partners-band{position:absolute;left:51px;top:0;width:1098px;height:317px;background:linear-gradient(180deg,#c9c1b5 0%,#e2ddd5 40%,#b9b0a3 100%)}
.partners .section-title{position:absolute;top:46px;width:1200px;text-align:center;color:#111}
.partners .section-sub{position:absolute;top:92px;width:1200px;text-align:center;color:#111}
.partner{position:absolute;top:121px;width:210px;height:196px}
.partner.a{background:linear-gradient(180deg,#48657a,#1f2a33)}
.partner.b{background:linear-gradient(180deg,#7f8a94,#3e4a55)}
.partner-feature{position:absolute;top:121px;left:520px;width:160px;height:196px;background:rgba(59,181,74,.9);color:var(--white);padding:22px 14px}
.partner-feature h3{font-family:"Open Sans",Arial,sans-serif;font-size:40px;font-weight:300;line-height:40px}
.partner-feature .role{font-size:12px;font-weight:700;margin-top:4px}
.partner-feature .link{font-size:12px;position:absolute;bottom:28px;left:14px}
.partner-feature svg{position:absolute;right:14px;bottom:18px}

/* links */
.links{top:2347px;height:403px;background:var(--paper-alt)}
.links .section-title{margin-top:50px}
.link-col{position:absolute;top:162px;list-style:none;text-align:left}
.link-col li{font-size:12.5px;line-height:32px;color:var(--ink)}
.link-col li.active{color:var(--green);text-decoration:underline}

/* map */
.map{top:2750px;height:334px;background:linear-gradient(180deg,#a9cbe8 0%,#b7d3ea 50%,#9fc3e2 100%)}
.map-button{position:absolute;left:10px;top:12px;background:var(--white);font-family:"Open Sans",Arial,sans-serif;font-size:11px;color:var(--blue);padding:4px 8px;box-shadow:0 1px 3px rgba(0,0,0,.3)}

/* contact */
.contact{top:3084px;height:513px;background:var(--dark);color:var(--white)}
.contact .section-title{margin-top:50px;font-family:"Open Sans",Arial,sans-serif}
.field{position:absolute;left:141px;width:450px;background:var(--field);color:#999;font-size:11px;padding:9px 12px}
.send{position:absolute;left:141px;top:429px;width:147px;height:39px;background:var(--green);color:var(--white);font-size:16px;text-align:center;line-height:39px;font-family:"Open Sans",Arial,sans-serif}
.contact-info{position:absolute;left:625px;top:150px;width:420px;font-size:12px;line-height:19px}
.contact-brand{display:flex;align-items:center;gap:10px;font-size:30px;color:var(--white)}
.contact-brand .brand-dot{width:50px;height:50px}
.contact-info h4{font-family:"Open Sans",Arial,sans-serif;font-size:15px;margin-top:20px;letter-spacing:1px}
.contact-info h4 span{font-weight:400}
.contact-info .item{display:flex;align-items:center;gap:6px;font-style:italic}
.contact-info .row{display:flex;gap:18px}
.contact-social{display:flex;gap:10px;margin-top:12px}
.contact-social span{width:30px;height:30px;border-radius:50%;background:#666}
.contact-social span.on{background:#3a87c8}
.footer-line{position:absolute;left:625px;top:474px;width:420px;border-top:1px solid #555}
.copyright{position:absolute;left:625px;top:483px;font-size:10px;color:#bbb}
.to-top{position:absolute;right:40px;top:455px;width:32px;height:32px;background:#888}
</style>
</head>
<body>

<section class="hero">
  <div class="hero-photo" role="img" aria-label="Photo of plumbing tools laid out on a wooden workbench"></div>
  <div class="hero-shade"></div>
  <div class="hero-brand">
    <div class="hero-mark"></div>
    <div class="hero-name">KalVeno</div>
    <div class="hero-tagline">— QUALITÉ PAR TRADITION —</div>
  </div>
  <div class="hero-badge">FIXING<br>24/7</div>
  <div class="hero-dots"><span></span><span class="active"></span><span></span><span></span></div>
  <svg class="hero-scroll" width="24" height="90" viewBox="0 0 24 90"><path d="M12 2 V88 M4 10 L12 2 L20 10 M4 80 L12 88 L20 80" stroke="#fff" stroke-width="2" fill="none"/></svg>
</section>

<header class="site-header">
  <div class="header-brand"><span class="brand-dot"></span>KalVeno</div>
  <div class="social"><span></span><span class="on"></span><span></span><span></span></div>
</header>

<section class="about center">
  <h2 class="section-title">WHO WE ARE</h2>
  <p class="section-sub">Welcome to KalVeno Plumbing</p>
  <div class="about-text">
    <p>Lorem ipsum dolor sit amet, consectetuer adipiscing elit, sed diam nonummy nibh euismod tincidunt ut laoreet dolore magna aliquam erat volutpat. Ut wisi enim ad minim veniam, quis nostrud exerci tation ullamcorper suscipit lobortis nisl ut aliquip ex ea commodo consequat. Duis autem vel eum iriure dolor in hendrerit in vulputate velit esse molestie consequat, vel illum dolore eu feugiat nulla facilisis at vero eros et accumsan et iusto odio dignissim qui blandit praesent luptatum zzril delenit augue duis dolore te feugait nulla facilisi.</p>
    <p>Duis autem vel eum iriure dolor in hendrerit in vulputate velit esse molestie consequat, vel illum dolore eu feugiat nulla facilisis at vero eros et accumsan et iusto odio dignissim qui blandit praesent luptatum zzril delenit augue duis dolore te feugait nulla facilisi.</p>
    <p>Illum dolore eu feugiat nulla facilisis at vero eros et accumsan et iusto odio dignissim qui blandit praesent luptatum zzril delenit augue duis dolore te feugait nulla facilisi.</p>
  </div>
</section>

<section class="news center">
  <div class="news-photo" role="img" aria-label="Photo of a bathroom tap in blue tones"></div>
  <h2 class="section-title">NEWS</h2>
  <div class="news-cards">
    <article class="news-card"><div class="news-thumb" role="img" aria-label="Photo of plumbing pipes"></div><h3>Latest News</h3><p>Dignissim qui blandit praesent luptatum zzril delenit augue duis dolore te feugait nulla facilisi.</p><a>Read more &gt; &gt;</a></article>
    <article class="news-card"><div class="news-thumb" role="img" aria-label="Photo of plumbing pipes"></div><h3>Latest News</h3><p>Dignissim qui blandit praesent luptatum zzril delenit augue duis dolore te feugait nulla facilisi.</p><a>Read more &gt; &gt;</a></article>
    <article class="news-card"><div class="news-thumb" role="img" aria-label="Photo of plumbing pipes"></div><h3>Latest News</h3><p>Dignissim qui blandit praesent luptatum zzril delenit augue duis dolore te feugait nulla facilisi.</p><a>Read more &gt; &gt;</a></article>
    <article class="news-card"><div class="news-thumb" role="img" aria-label="Photo of plumbing pipes"></div><h3>Latest News</h3><p>Dignissim qui blandit praesent luptatum zzril delenit augue duis dolore te feugait nulla facilisi.</p><a>Read more &gt; &gt;</a></article>
    <article class="news-card"><div class="news-thumb" role="img" aria-label="Photo of plumbing pipes"></div><h3>Latest News</h3><p>Dignissim qui blandit praesent luptatum zzril delenit augue duis dolore te feugait nulla facilisi.</p><a>Read more &gt; &gt;</a></article>
  </div>
</section>

<section class="services center">
  <h2 class="section-title">SERVICES WE PROVIDE</h2>
  <p class="section-sub">Our Main focus is on Fixing 24/7</p>

  <div class="service" style="left:140px;top:204px">
    <svg width="92" height="92" viewBox="0 0 92 92"><circle cx="46" cy="46" r="42" fill="none" stroke="#333" stroke-width="4"/><path d="M28 28 L64 64 M64 28 L28 64" stroke="#333" stroke-width="7" stroke-linecap="round"/></svg>
    <h3>Service Maintenance</h3>
    <p>Lorem ipsum dolor sit amet, consectetuer adipiscing elit. Nam vel turpis. Duis sit amet lectus ac mauris porta viverra.</p>
  </div>
  <div class="service" style="left:450px;top:204px">
    <svg width="92" height="92" viewBox="0 0 92 92"><circle cx="46" cy="46" r="42" fill="none" stroke="#333" stroke-width="4"/><path d="M22 36 H56 V50 M40 36 V26 M32 26 H48 M56 56 V62" stroke="#333" stroke-width="7" fill="none" stroke-linecap="round"/></svg>
    <h3>Sanitary</h3>
    <p>Lorem ipsum dolor sit amet, consectetuer adipiscing elit. Nam vel turpis. Duis sit amet lectus ac mauris porta viverra.</p>
  </div>
  <div class="service" style="left:765px;top:204px">
    <svg width="92" height="92" viewBox="0 0 92 92"><circle cx="46" cy="46" r="42" fill="none" stroke="#333" stroke-width="4"/><circle cx="46" cy="46" r="14" fill="none" stroke="#333" stroke-width="6"/><path d="M18 46 H32 M60 46 H74 M46 46 L52 38" stroke="#333" stroke-width="6" stroke-linecap="round"/></svg>
    <h3>Renewable Energy</h3>
    <p>Lorem ipsum dolor sit amet, consectetuer adipiscing elit. Nam vel turpis. Duis sit amet lectus ac mauris porta viverra.</p>
  </div>
  <div class="service" style="left:140px;top:492px">
    <svg width="92" height="92" viewBox="0 0 92 92"><circle cx="46" cy="46" r="42" fill="none" stroke="#333" stroke-width="4"/><path d="M46 20 V56 M30 56 H62 V66 H30 Z" stroke="#333" stroke-width="6" fill="none" stroke-linejoin="round"/></svg>
    <h3>Heating</h3>
    <p>Lorem ipsum dolor sit amet, consectetuer adipiscing elit. Nam vel turpis. Duis sit amet lectus ac mauris porta viverra.</p>
  </div>
  <div class="service" style="left:450px;top:492px">
    <svg width="92" height="92" viewBox="0 0 92 92"><circle cx="46" cy="46" r="42" fill="none" stroke="#333" stroke-width="4"/><circle cx="46" cy="46" r="26" fill="none" stroke="#333" stroke-width="5"/><path d="M46 46 L46 24 M46 46 L66 54 M46 46 L28 60" stroke="#333" stroke-width="5" stroke-linecap="round"/></svg>
    <h3>Ventilation</h3>
    <p>Lorem ipsum dolor sit amet, consectetuer adipiscing elit. Nam vel turpis. Duis sit amet lectus ac mauris porta viverra.</p>
  </div>
  <div class="service" style="left:765px;top:492px">
    <svg width="92" height="92" viewBox="0 0 92 92"><circle cx="46" cy="46" r="42" fill="none" stroke="#333" stroke-width="4"/><path d="M46 20 V72 M23 33 L69 59 M23 59 L69 33" stroke="#333" stroke-width="6" stroke-linecap="round"/></svg>
    <h3>Air Conditioning</h3>
    <p>Lorem ipsum dolor sit amet, consectetuer adipiscing elit. Nam vel turpis. Duis sit amet lectus ac mauris porta viverra.</p>
  </div>
</section>

<section class="partners">
  <div class="partners-band" role="img" aria-label="Illustration of tools around the partners area"></div>
  <h2 class="section-title">OUR PARTNERS</h2>
  <p class="section-sub">Our Main focus is on Fixing 24/7</p>
  <div class="partner a" style="left:100px" role="img" aria-label="Portrait of a partner in a hard hat"></div>
  <div class="partner b" style="left:310px" role="img" aria-label="Portrait of a partner"></div>
  <div class="partner b" style="left:680px" role="img" aria-label="Portrait of a partner"></div>
  <div class="partner a" style="left:890px" role="img" aria-label="Portrait of a partner in a hard hat"></div>
  <div class="partner-feature">
    <h3>John<br>Doe</h3>
    <div class="role">Media partner</div>
    <div class="link">View Profile</div>
    <svg width="40" height="40" viewBox="0 0 40 40"><circle cx="20" cy="20" r="13" fill="none" stroke="#fff" stroke-width="3"/><path d="M20 2 V38 M2 20 H38" stroke="#fff" stroke-width="3"/></svg>
  </div>
</section>

<section class="links center">
  <h2 class="section-title">USEFUL LINKS</h2>
  <p class="section-sub">Following are the links</p>
  <ul class="link-col" style="left:160px">
    <li>Lorem Ipsum</li><li>Dolor Sit Amet,</li><li>Lectus Ac Mauris Porta Viverra.</li><li>Consectetuer Adipiscing Elit.</li><li>Nam Vel Turpis.</li><li>Duis Sit Amet</li>
  </ul>
  <ul class="link-col" style="left:465px">
    <li>Lorem Ipsum</li><li>Dolor Sit Amet,</li><li class="active">Lectus Ac Mauris Porta Viverra.</li><li>Consectetuer Adipiscing Elit.</li><li>Nam Vel Turpis.</li><li>Duis Sit Amet</li>
  </ul>
  <ul class="link-col" style="left:771px">
    <li>Lorem Ipsum</li><li>Dolor Sit Amet,</li><li>Lectus Ac Mauris Porta Viverra.</li>
  </ul>
</section>

<section class="map" role="img" aria-label="World map showing the company location">
  <div class="map-button">View on Ordenmap</div>
</section>

<section class="contact">
  <h2 class="section-title center">CONTACT US</h2>
  <p class="section-sub center">Using the contact form to send us email at below</p>
  <div class="contact-form">
    <div class="field" style="top:146px;height:35px">Name*</div>
    <div class="field" style="top:191px;height:35px">Email*</div>
    <div class="field" style="top:236px;height:185px">Message</div>
    <div class="send">SEND</div>
  </div>
  <div class="contact-info">
    <div class="contact-brand"><span class="brand-dot"></span>KalVeno</div>
    <h4>KEEP IN TOUCH <span>WITH US</span></h4>
    <p>You can use the following information to contact us if you wanna join us or anything need to communicate</p>
    <div class="item" style="margin-top:6px"><svg width="12" height="12"><rect width="12" height="12" fill="#3bb54a"/></svg>KalVeno Plumbing</div>
    <div class="row">
      <div class="item"><svg width="10" height="14"><rect x="1" y="0" width="8" height="14" rx="2" fill="#3bb54a"/></svg>12 7 61 48 20</div>
      <div class="item"><svg width="10" height="14"><rect x="1" y="0" width="8" height="14" rx="2" fill="#3bb54a"/></svg>24 58 19 72 06</div>
    </div>
    <div class="item"><svg width="10" height="14" viewBox="0 0 10 14"><path d="M5 14 L1 7 A4 4 0 1 1 9 7 Z" fill="#3bb54a"/></svg>Address : NO.86,XX Road,XX City,Country</div>
    <div class="contact-social"><span></span><span class="on"></span><span></span></div>
  </div>
  <div class="footer-line"></div>
  <div class="copyright">COPYRIGHT © 2014 KALVENO INC.</div>
  <div class="to-top"><svg width="32" height="32"><path d="M9 19 L16 12 L23 19" stroke="#fff" stroke-width="3" fill="none"/></svg></div>
</section>

</body>
</html>
```